Business Card Design Project

Keep it simple , using logo and colors that compliment. Logo on one side with complimentary back ground color. Other side, personal info with possible complimentary design/colors

Target Market(s)

we are a non for profit that will be seeking donations . Both monetary and in kind

Industry/Entity Type

Business

Font styles to use
Sans Serif

Colors

Designer to choose colors to be used in the design.

```html
<!DOCTYPE html>
<html lang="en">
<head>
<meta charset="utf-8">
<title>Open Hand Trust – Business Card</title>
<link rel="stylesheet" href="https://fonts.googleapis.com/css2?family=Lato:wght@400;700;900&display=swap">
<style>
  :root {
    --navy: #1d2347;
    --gold: #e8d312;
    --paper: #ffffff;
    --paper-shade: #eeeeef;
    --stage: #e4e5e8;
    --ink-light: #e9eaf2;
  }
  * { box-sizing: border-box; margin: 0; padding: 0; }
  html, body {
    width: 1200px; height: 997px; overflow: hidden;
    background: var(--stage);
    font-family: "Lato", sans-serif;
  }
  .sheet {
    position: relative; width: 1200px; height: 997px;
    display: flex; align-items: center; justify-content: center; gap: 40px;
  }
  .card {
    position: relative; width: 540px; height: 310px;
    border-radius: 26px; overflow: hidden;
    box-shadow: 0 14px 30px rgba(20, 24, 50, 0.22);
  }

  /* Brand name set as plain text with a single dot */
  .brand {
    display: flex; align-items: center; gap: 10px;
    white-space: nowrap;
  }
  .brand__dot {
    width: 16px; height: 16px; border-radius: 50%;
    background: var(--gold); flex: none;
  }
  .brand__name {
    font-family: "Lato", sans-serif; font-weight: 400;
  }

  /* Logo side */
  .card--logo {
    background: var(--navy);
    display: flex; align-items: center; justify-content: center;
  }
  .card--logo .brand__name { color: var(--gold); font-size: 36px; }

  /* Info side */
  .card--info { background: var(--navy); display: flex; }
  .card__panel {
    width: 232px; height: 100%; flex: none;
    background: linear-gradient(180deg, var(--paper), var(--paper-shade));
    display: flex; align-items: center; justify-content: center;
  }
  .card__panel .brand { gap: 8px; }
  .card__panel .brand__dot { width: 12px; height: 12px; }
  .card__panel .brand__name { color: var(--navy); font-size: 22px; }
  .card__stripes { width: 24px; height: 100%; display: block; flex: none; }
  .card__details {
    flex: 1; padding: 36px 0 0 22px; color: var(--ink-light);
  }
  .person__name { font-weight: 900; font-size: 17px; letter-spacing: 0.5px; color: #fff; }
  .person__title { font-weight: 700; font-size: 11.5px; letter-spacing: 0.6px; margin: 3px 0 0 14px; color: #fff; }
  .contact-list { list-style: none; margin-top: 88px; }
  .contact-list li {
    display: flex; align-items: center; gap: 7px;
    font-size: 13.5px; line-height: 24px; color: var(--ink-light);
    white-space: nowrap;
  }
  .contact-list svg { width: 14px; height: 14px; flex: none; }
</style>
</head>
<body>
<main class="sheet">
  <section class="card card--logo" aria-label="Card front">
    <div class="brand"><span class="brand__dot"></span><span class="brand__name">Open Hand Trust</span></div>
  </section>

  <section class="card card--info" aria-label="Card back">
    <div class="card__panel">
      <div class="brand"><span class="brand__dot"></span><span class="brand__name">Open Hand Trust</span></div>
    </div>
    <svg class="card__stripes" viewBox="0 0 24 310" preserveAspectRatio="none" aria-hidden="true">
      <rect width="24" height="310" fill="#ffffff"/>
      <rect x="3" width="3" height="310" fill="#1d2347"/>
      <rect x="10" width="3" height="310" fill="#1d2347"/>
      <rect x="17" width="3" height="310" fill="#1d2347"/>
    </svg>
    <div class="card__details">
      <p class="person__name">DANIEL MOREAU</p>
      <p class="person__title">MANAGING DIRECTOR</p>
      <ul class="contact-list">
        <li>
          <svg viewBox="0 0 16 16" aria-hidden="true"><path d="M2 5c0-2 2-3 6-3s6 1 6 3v1h-3V5H5v1H2z M4 8h8l2 5H2z" fill="#e9eaf2"/></svg>
          +61 400 555 017
        </li>
        <li>
          <svg viewBox="0 0 16 16" aria-hidden="true"><rect x="1" y="3" width="14" height="10" fill="#e9eaf2"/><path d="M1 3l7 6 7-6" fill="none" stroke="#1d2347" stroke-width="1.4"/></svg>
          daniel@openhandtrust.org.au
        </li>
        <li>
          <svg viewBox="0 0 16 16" aria-hidden="true"><g fill="none" stroke="#e9eaf2" stroke-width="1.6"><rect x="1.5" y="7" width="8" height="4" rx="2" transform="rotate(-40 5.5 9)"/><rect x="6.5" y="5" width="8" height="4" rx="2" transform="rotate(-40 10.5 7)"/></g></svg>
          www.openhandtrust.org.au
        </li>
        <li>
          <svg viewBox="0 0 16 16" aria-hidden="true"><circle cx="8" cy="8" r="4" fill="#e9eaf2"/></svg>
          social: /openhandtrust
        </li>
      </ul>
    </div>
  </section>
</main>
</body>
</html>
```